Professional Services/Construction Management (Millwork) Biz Cards

We've decided on a logo and have our color palette set, now we want to design some very professional looking cards that make a strong first impression - they'll reflect our tagline (that we're going to put on the back: Innovative. Professional. Leaders.

The example business card shows generally the direction we've been thinking of going for the back side - **but we're open to other ideas**

Target Market(s)

The cards should target more high-end (wealthy) owners and general contracting companies. We want them to convey a strong first impression - in a professional and not garish way.

Industry/Entity Type

Construction Company

Contact Information for Business Card

There needs to be a place for our company contractor's license number and business address. We want to also have people's names, titles, phone number, email address. The back can be the logo, tagline and web address

Requirements
Must have
• follow our color palette
Nice to have
• Font & Styles should compliment the Harrow Joinery fonts, but not necessarily match exactly

```html
<!DOCTYPE html>
<html lang="en">
<head>
<meta charset="utf-8">
<title>Harrow Joinery – Business Cards</title>
<link rel="stylesheet" href="https://fonts.googleapis.com/css2?family=Ubuntu:wght@400;500;700&family=Open+Sans:ital,wght@1,600;1,700&display=swap">
<style>
  :root {
    --backdrop: #4a4a4a;
    --card-white: #ffffff;
    --brand-brown: #5e4f42;
    --brand-green: #4e9a35;
    --brand-mauve: #a3877f;
    --rule-grey: #8a7f76;
    --text-grey: #5b5653;
    --text-white: #ffffff;
  }
  * { margin: 0; padding: 0; box-sizing: border-box; }
  html, body {
    width: 1105px; height: 1200px; overflow: hidden;
    background: var(--backdrop);
    font-family: "Ubuntu", sans-serif;
  }
  .stage { position: relative; width: 1105px; height: 1200px; }

  .card {
    position: absolute; left: 192px; width: 720px; height: 412px;
    border-radius: 20px; overflow: hidden;
  }
  .card--front { top: 146px; background: var(--card-white); }
  .card--back  { top: 600px; background: var(--brand-brown); }

  /* front */
  .brand {
    position: absolute; left: 43px; top: 104px;
    display: flex; align-items: center; gap: 14px;
  }
  .brand__dot { width: 46px; height: 46px; border-radius: 50%; background: var(--brand-brown); }
  .brand__name { font-weight: 700; font-size: 30px; color: var(--brand-brown); letter-spacing: 0.5px; }

  .rule { position: absolute; height: 2px; top: 258px; }
  .rule--grey { left: 43px; width: 510px; background: var(--rule-grey); }
  .rule--green { left: 553px; width: 126px; background: var(--brand-green); }

  .side-tab { position: absolute; left: 704px; top: 208px; width: 16px; height: 53px; background: var(--brand-brown); }

  .person { position: absolute; right: 41px; top: 196px; text-align: right; }
  .person__name { font-weight: 700; font-size: 25px; color: var(--brand-brown); line-height: 30px; }
  .person__title { font-size: 19px; color: var(--brand-green); line-height: 26px; }

  .contacts, .company-details {
    position: absolute; top: 276px; list-style: none;
    font-size: 18px; color: var(--text-grey); line-height: 28px;
  }
  .contacts { left: 43px; }
  .contacts li { display: flex; align-items: center; gap: 12px; }
  .contacts svg { width: 18px; height: 18px; fill: var(--brand-brown); }
  .company-details { right: 41px; text-align: right; }

  .base-band { position: absolute; left: 0; bottom: 0; width: 720px; height: 28px; }

  /* back */
  .back-brand {
    position: absolute; left: 0; right: 0; top: 150px;
    display: flex; justify-content: center; align-items: center; gap: 16px;
  }
  .back-brand__dot { width: 52px; height: 52px; border-radius: 50%; background: var(--brand-mauve); }
  .back-brand__name { font-weight: 700; font-size: 38px; color: var(--text-white); letter-spacing: 0.5px; }
  .tagline {
    position: absolute; left: 0; right: 0; top: 274px; text-align: center;
    font-family: "Open Sans", sans-serif; font-style: italic; font-weight: 700;
    font-size: 20px; color: var(--text-white);
  }
  .back-web {
    position: absolute; left: 0; right: 0; top: 302px; text-align: center;
    font-family: "Open Sans", sans-serif; font-style: italic; font-weight: 600;
    font-size: 18px; letter-spacing: 1px; color: var(--text-white);
  }
</style>
</head>
<body>
<main class="stage">
  <section class="card card--front" aria-label="Business card front">
    <div class="brand">
      <span class="brand__dot"></span>
      <span class="brand__name">Harrow Joinery</span>
    </div>

    <div class="person">
      <p class="person__name">DANIEL REEVE</p>
      <p class="person__title">CEO/Founder</p>
    </div>
    <div class="rule rule--grey"></div>
    <div class="rule rule--green"></div>
    <div class="side-tab"></div>

    <ul class="contacts">
      <li>
        <svg viewBox="0 0 24 24" aria-hidden="true"><path d="M6.6 10.8a15.1 15.1 0 0 0 6.6 6.6l2.2-2.2c.3-.3.7-.4 1-.2 1.1.4 2.3.6 3.6.6.6 0 1 .4 1 1V20c0 .6-.4 1-1 1A17 17 0 0 1 3 4c0-.6.4-1 1-1h3.5c.6 0 1 .4 1 1 0 1.3.2 2.5.6 3.6.1.3 0 .7-.2 1l-2.3 2.2z"/></svg>
        <span>555 014 2290</span>
      </li>
      <li>
        <svg viewBox="0 0 24 24" aria-hidden="true"><path d="M3 6h18v12H3z M3 6l9 7 9-7" fill="none" stroke="#5e4f42" stroke-width="2"/></svg>
        <span>hello@harrowjoinery.com</span>
      </li>
      <li>
        <svg viewBox="0 0 24 24" aria-hidden="true"><circle cx="12" cy="12" r="10"/><path d="M2 12h20M12 2c3 3 3 17 0 20M12 2c-3 3-3 17 0 20" fill="none" stroke="#fff" stroke-width="1.5"/></svg>
        <span>www.harrowjoinery.com</span>
      </li>
    </ul>

    <ul class="company-details">
      <li>lic no 40218857</li>
      <li>412 Birchwood Road</li>
      <li>Juneau, Alaska 99801</li>
    </ul>

    <svg class="base-band" viewBox="0 0 720 28" preserveAspectRatio="none" aria-hidden="true">
      <polygon points="0,0 464,0 456,28 0,28" fill="var(--brand-brown)"/>
      <polygon points="472,0 720,0 720,28 464,28" fill="var(--brand-green)"/>
    </svg>
  </section>

  <section class="card card--back" aria-label="Business card back">
    <div class="back-brand">
      <span class="back-brand__dot"></span>
      <span class="back-brand__name">Harrow Joinery</span>
    </div>
    <p class="tagline">Innovative. Professional. Leaders.</p>
    <p class="back-web">www.harrowjoinery.com</p>
  </section>
</main>
</body>
</html>
```